Business Card for mobile spray tan service
Mist Aurora
Use same font as used in my logo
or complimenting fonts
Modern
Marlene Oduya
Spray Technician
4072 Amber Willow Lane
Suite C
Chesapeake, Virginia 23487
auroramist@fernpost.example
In the logos provided, I included a Bramwick logo which is the product I use. Would like to somehow make that work on the card but not large. Would like to see fonts that compliment the logo but not the same necessarily

```html
<!DOCTYPE html>
<html lang="en">
<head>
<meta charset="utf-8">
<title>Mist Aurora – Business Card</title>
<link rel="stylesheet" href="https://fonts.googleapis.com/css2?family=Open+Sans:wght@400;600;700&display=swap">
<style>
  :root {
    --page-bg: #e9e6e2;
    --card-bg: #ffffff;
    --brand-brown: #8b4a34;
    --brand-grey: #8c8c8c;
    --text-dark: #4a4a4a;
    --text-muted: #7a7a7a;
    --divider: #9a9a9a;
  }
  * { margin: 0; padding: 0; box-sizing: border-box; }
  html, body {
    width: 1200px;
    height: 914px;
    overflow: hidden;
    background: var(--page-bg);
    font-family: "Open Sans", Arial, sans-serif;
  }
  .card {
    position: absolute;
    left: 75px;
    top: 157px;
    width: 1050px;
    height: 600px;
    background: var(--card-bg);
    box-shadow: 0 6px 24px rgba(0,0,0,0.12);
    overflow: hidden;
  }
  .brand {
    position: absolute;
    left: 470px;
    top: 150px;
    display: flex;
    align-items: center;
    gap: 14px;
  }
  .brand-dot {
    width: 34px;
    height: 34px;
    border-radius: 50%;
    background: var(--brand-brown);
  }
  .brand-name {
    font-weight: 600;
    font-size: 66px;
    line-height: 1;
    color: var(--brand-brown);
    letter-spacing: -0.5px;
  }
  .brand-tagline {
    position: absolute;
    left: 560px;
    top: 236px;
    font-size: 26px;
    color: var(--brand-brown);
    letter-spacing: 0.5px;
  }
  .identity {
    position: absolute;
    left: 34px;
    top: 318px;
    display: flex;
    align-items: center;
    font-size: 27px;
    color: var(--brand-brown);
  }
  .identity-name { font-weight: 700; }
  .identity-sep {
    width: 3px;
    height: 30px;
    margin: 0 12px;
    background: var(--brand-brown);
  }
  .identity-role { font-weight: 400; }
  .contact-divider {
    position: absolute;
    left: 448px;
    top: 366px;
    width: 2px;
    height: 150px;
    background: var(--divider);
  }
  .contact-list {
    position: absolute;
    left: 466px;
    top: 364px;
    list-style: none;
    font-size: 22px;
    line-height: 1.45;
    color: var(--text-dark);
  }
  .contact-item {
    display: flex;
    align-items: flex-start;
    gap: 10px;
  }
  .contact-item .icon {
    flex: none;
    width: 22px;
    height: 22px;
    margin-top: 5px;
  }
  .contact-item .indent { padding-left: 32px; }
  .footer-bands {
    position: absolute;
    left: 0;
    bottom: 0;
    width: 1050px;
    height: 90px;
  }
</style>
</head>
<body>
  <main class="card">
    <div class="brand">
      <span class="brand-dot"></span>
      <span class="brand-name">MistAurora</span>
    </div>
    <p class="brand-tagline">mobile spray tan service</p>

    <div class="identity">
      <span class="identity-name">Marlene Oduya</span>
      <span class="identity-sep"></span>
      <span class="identity-role">Spray Technician</span>
    </div>

    <div class="contact-divider"></div>
    <ul class="contact-list">
      <li class="contact-item">
        <svg class="icon" viewBox="0 0 22 22" aria-hidden="true">
          <circle cx="11" cy="11" r="11" fill="var(--brand-brown)"/>
          <path d="M11 5a4 4 0 0 0-4 4c0 3 4 8 4 8s4-5 4-8a4 4 0 0 0-4-4zm0 5.5a1.5 1.5 0 1 1 0-3 1.5 1.5 0 0 1 0 3z" fill="#fff"/>
        </svg>
        <span>4072 Amber Willow Lane Suite C</span>
      </li>
      <li class="contact-item"><span class="indent">Chesapeake, Virginia 23487</span></li>
      <li class="contact-item">
        <svg class="icon" viewBox="0 0 22 22" aria-hidden="true">
          <circle cx="11" cy="11" r="11" fill="var(--brand-brown)"/>
          <path d="M7.5 5.5l2 2-1.2 1.6c.7 1.6 1.9 2.8 3.5 3.5l1.6-1.2 2 2-1.3 2.1c-4.3-.3-8.1-4.1-8.4-8.4z" fill="#fff"/>
        </svg>
        <span>757-555-0148</span>
      </li>
      <li class="contact-item">
        <svg class="icon" viewBox="0 0 22 22" aria-hidden="true">
          <circle cx="11" cy="11" r="11" fill="var(--brand-brown)"/>
          <rect x="5.5" y="7" width="11" height="8" rx="1" fill="#fff"/>
          <path d="M5.5 7.5l5.5 4 5.5-4" fill="none" stroke="var(--brand-brown)" stroke-width="1.2"/>
        </svg>
        <span>auroramist@fernpost.example</span>
      </li>
    </ul>

    <svg class="footer-bands" viewBox="0 0 1050 90" aria-hidden="true">
      <polygon points="0,20 455,20 430,56 0,56" fill="var(--brand-brown)"/>
      <polygon points="470,36 1050,36 1050,72 445,72" fill="var(--brand-grey)"/>
    </svg>
  </main>
</body>
</html>
```